Personal Finance e-commerce website needs a simple budget design

Hello! I am starting to sell downloadable and printable budget planners, as shown in the attached file, for people to plan ahead on their personal finances. <br/><br/>I want to see a one-page design with similar columns (for example, "Expenses, Budget, and Actual"). I would also like to see the basic formula ("Net Income = Gross income - Total Expenses") somewhere on the design. Finally, I want the design to remain mostly minimalistic and simple for the average person to plan their personal monthly budgets.<br/><br/>However, other than that, the overall design, layout, and colors will be at the graphic designer's choice. If you have any questions for me, please let me know. Thank you for your time!

Industry/Entity Type

Financial Planning

Colors

Designer to choose colors to be used in the design.

Requirements
Must have
• I want to see a one-page design with similar columns (for example, "Expenses, Budget, and Actual").
• I want the design to remain mostly minimalistic and simple for the average person to plan their personal monthly budgets.
Nice to have
• I would also like to see the basic formula ("Net Income = Gross income - Total Expenses") somewhere on the design.

```html
<!DOCTYPE html>
<html lang="en">
<head>
<meta charset="utf-8">
<title>Basic Monthly Budget</title>
<link href="https://fonts.googleapis.com/css2?family=Roboto:wght@400;500;700&display=swap" rel="stylesheet">
<style>
  :root {
    --ink: #000000;
    --text: #1a1a1a;
    --muted: #5f5f5f;
    --faint: #9a9a9a;
    --rule: #8a8a8a;
    --paper: #ffffff;
  }
  * { margin: 0; padding: 0; box-sizing: border-box; }
  html, body { width: 849px; height: 1200px; overflow: hidden; background: var(--paper); }
  body { font-family: "Roboto", Arial, sans-serif; color: var(--text); }
  .sheet { position: relative; width: 849px; height: 1200px; }

  .brand {
    position: absolute; left: 77px; top: 84px;
    font-size: 34px; font-weight: 700; line-height: 36px; color: var(--ink);
  }
  .doc-title {
    position: absolute; right: 77px; top: 84px;
    font-size: 15.5px; font-weight: 500; letter-spacing: 1.2px; color: #333;
  }
  .date-field {
    position: absolute; right: 77px; top: 128px;
    display: flex; gap: 16px; align-items: flex-start;
  }
  .date-field span {
    display: block; border-top: 1.5px solid #222;
    padding-top: 3px; font-size: 16px; letter-spacing: 1.5px; color: var(--faint);
  }
  .date-field .mm { width: 36px; }
  .date-field .yyyy { width: 53px; text-align: right; }
  .slash { position: absolute; right: 127px; top: 132px; font-size: 16px; color: var(--faint); }

  .grid { position: absolute; left: 0; top: 0; }

  .col-head { position: absolute; top: 212px; }
  .col-head h2 { font-size: 19.5px; font-weight: 500; color: var(--ink); line-height: 26px; }
  .col-head p { font-size: 15px; color: var(--muted); margin-top: 5px; }
  .col-expenses { left: 77px; }
  .col-budget { left: 370px; }
  .col-actual { left: 579px; }

  .formula { position: absolute; top: 1027px; text-align: center; }
  .formula h3 { font-size: 19.5px; font-weight: 500; color: var(--ink); line-height: 26px; }
  .formula p { font-size: 15px; color: var(--muted); line-height: 17px; margin-top: 2px; }
  .f-net { left: 109px; width: 160px; }
  .f-gross { left: 344px; width: 160px; }
  .f-total { left: 575px; width: 160px; }
  .operator { position: absolute; }

  .footer {
    position: absolute; left: 0; width: 849px; top: 1123px;
    text-align: center; font-size: 15px; color: var(--faint);
  }
  .footer .site { color: var(--text); border-bottom: 1px dashed var(--faint); }
</style>
</head>
<body>
<main class="sheet">
  <div class="brand">Carla<br>Denby</div>
  <div class="doc-title">BASIC MONTHLY BUDGET</div>
  <div class="date-field"><span class="mm">MM</span><span class="yyyy">YYYY</span></div>
  <div class="slash">/</div>

  <svg class="grid" width="849" height="1200" viewBox="0 0 849 1200" aria-hidden="true">
    <g stroke="var(--rule)" stroke-width="1.4">
      <line x1="354.5" y1="199" x2="354.5" y2="998"/>
      <line x1="563.5" y1="199" x2="563.5" y2="998"/>
      <line x1="77" y1="338.8" x2="772" y2="338.8"/>
      <line x1="77" y1="398.7" x2="772" y2="398.7"/>
      <line x1="77" y1="458.6" x2="772" y2="458.6"/>
      <line x1="77" y1="518.5" x2="772" y2="518.5"/>
      <line x1="77" y1="578.4" x2="772" y2="578.4"/>
      <line x1="77" y1="638.3" x2="772" y2="638.3"/>
      <line x1="77" y1="698.2" x2="772" y2="698.2"/>
      <line x1="77" y1="758.1" x2="772" y2="758.1"/>
      <line x1="77" y1="818" x2="772" y2="818"/>
      <line x1="77" y1="877.9" x2="772" y2="877.9"/>
      <line x1="77" y1="937.8" x2="772" y2="937.8"/>
      <line x1="77" y1="997.5" x2="772" y2="997.5"/>
    </g>
    <rect x="77" y="274" width="695" height="5" fill="var(--ink)"/>
    <g fill="var(--muted)">
      <rect x="295" y="1049" width="20" height="4"/>
      <rect x="295" y="1058" width="20" height="4"/>
      <rect x="537" y="1053" width="12" height="4"/>
    </g>
  </svg>

  <div class="col-head col-expenses"><h2>Expenses (Category)</h2><p>Custom Category</p></div>
  <div class="col-head col-budget"><h2>Budget (USD)</h2><p>What you plan to spend</p></div>
  <div class="col-head col-actual"><h2>Actual (USD)</h2><p>What you actually spent</p></div>

  <div class="formula f-net"><h3>Net income</h3><p>How much money<br>you kept.</p></div>
  <div class="formula f-gross"><h3>Gross income</h3><p>How much money<br>you earned.</p></div>
  <div class="formula f-total"><h3>Total Expenses</h3><p>Actual expenses.</p></div>

  <p class="footer">Visit us at <span class="site">carladenby.com</span> for personal financial advice!</p>
</main>
</body>
</html>
```